Professional Oral Surgery Referral Pad, Business Card, and Stationary Design

Hello,

I want to work with a designer for my startup Oral Surgery Practice called: Redmont Creek Oral Surgery & Implant Center

Ideally I would like to choose a good/professional design and work with a designer all the way to fulfill ALL of our stationary needs including referral pads, business cards, letterheads, envelopes, notepads, email signature, etc.

I would like to see designs first and hopefully would like to work with the designer for the lifetime of my practice and wanting to develop a long-term professional relationship.

In terms of the logo I have attached our practice logo files: I want to stay within the 3 colorways of the logo: Navy Blue/Silver grey/White. I would like for you to be creative and incorporate the "V" as best you can (for example greyed out watermark, etc)

I have also attached in my files the full contact info of our office in a word document: which includes address, email address, phone, fax, cell, etc.

I have also attached a few examples of double sided referral pad we can draw inspiration from. In terms of the referral pad I would ideally like to have my logo nicely placed/incorporated to make it look professional, address of the practice and contact info, my name and credentials.

Referral pad must have lines for patient, date of birth, phone number, referring doctor name, odontogram of all adult teeth and pediatric teeth, nice and big - so easy for dentist to refer. Also a jaw drawing of the intraoral cavity. Below that should have comments to surgeon.

In terms of procedures, I would like to have options of IV sedation, extractions, wisdom teeth, bone graft, pathology, tmj, trauma, expose/bond, orthognathic, other (list below)

In the back we can have a greyed out map of my practice address and Instructions for patients should include to bring insurance documentation, medication list, etc.

The final nitty gritty details of the referral pad can be worked on once I am happy with the design.

Target Market(s)

Patients who need oral surgical services and dentist referrals

Industry/Entity Type

Oral and Maxillofacial Surgery

Font styles to use
Other font styles liked:
• I would leave it up to the designers!

Colors
0054AA
0677BA
7BADD7
CADEEF
E8F1F8

Requirements
Must have
• Professional/sleek/modern and three color ways same as logo (navy blue, silver gray, and white)
Nice to have
• I would like to highlight my logo especially the implant ā€œvā€ either as watermark or part of the header or footnote. I will leave it to the expertise of the designer

```html
<!DOCTYPE html>
<html lang="en">
<head>
<meta charset="utf-8">
<title>Email Signature – Redmont Creek Oral Surgery &amp; Implant Center</title>
<link href="https://fonts.googleapis.com/css2?family=Raleway:wght@700&family=Roboto:wght@400&display=swap" rel="stylesheet">
<style>
  :root {
    --navy: #1f3f86;
    --backdrop: #e6e7e9;
    --paper: #ffffff;
    --ink: #555558;
    --rule: #8a8a8c;
    --shadow: rgba(0, 0, 0, 0.35);
  }
  * { margin: 0; padding: 0; box-sizing: border-box; }
  html, body {
    width: 1200px;
    height: 1200px;
    overflow: hidden;
    background: var(--backdrop);
  }
  .canvas {
    position: relative;
    width: 1200px;
    height: 1200px;
  }
  .section-title {
    position: absolute;
    top: 347px;
    left: 0;
    width: 1200px;
    text-align: center;
    font-family: "Raleway", sans-serif;
    font-weight: 700;
    font-size: 31px;
    letter-spacing: -0.3px;
    color: var(--navy);
  }
  .signature {
    position: absolute;
    left: 223px;
    top: 462px;
    width: 754px;
    height: 276px;
    background: var(--paper);
    box-shadow: 4px 5px 7px var(--shadow);
    font-family: "Roboto", sans-serif;
    color: var(--ink);
  }
  .practice-mark {
    position: absolute;
    right: 61px;
    top: 48px;
    display: flex;
    align-items: center;
    gap: 12px;
  }
  .practice-mark__square {
    width: 14px;
    height: 14px;
    background: var(--navy);
  }
  .practice-mark__name {
    font-family: "Raleway", sans-serif;
    font-weight: 700;
    font-size: 19px;
    line-height: 24px;
    color: var(--navy);
    text-align: right;
  }
  .doctor-name {
    position: absolute;
    left: 63px;
    top: 105px;
    font-family: "Raleway", sans-serif;
    font-weight: 700;
    font-size: 21px;
    color: var(--navy);
  }
  .doctor-role {
    position: absolute;
    left: 63px;
    top: 130px;
    font-size: 19px;
  }
  .divider {
    position: absolute;
    left: 63px;
    top: 164px;
    width: 629px;
    height: 1.5px;
    background: var(--rule);
  }
  .address {
    position: absolute;
    left: 62px;
    top: 186px;
    font-size: 19px;
    line-height: 24px;
  }
  .contact-list {
    position: absolute;
    top: 189px;
    list-style: none;
    font-size: 19px;
    line-height: 26px;
  }
  .contact-list--phones { left: 277px; }
  .contact-list--web { left: 444px; }
  .contact-list li {
    display: flex;
    align-items: center;
    gap: 8px;
  }
  .contact-list svg {
    width: 21px;
    height: 19px;
    fill: var(--navy);
    flex: none;
  }
</style>
</head>
<body>
<main class="canvas">
  <h1 class="section-title">EMAIL SIGNATURE.</h1>

  <section class="signature">
    <div class="practice-mark">
      <span class="practice-mark__square"></span>
      <p class="practice-mark__name">Redmont Creek Oral Surgery<br>&amp; Implant Center</p>
    </div>

    <p class="doctor-name">Daniel R Hartley, DDS</p>
    <p class="doctor-role">Oral &amp; Maxillofacial Surgeon</p>

    <div class="divider"></div>

    <p class="address">1180 Willow Bend Rd<br>Redmont, CA 91402</p>

    <ul class="contact-list contact-list--phones">
      <li>
        <svg viewBox="0 0 24 22" aria-hidden="true"><path d="M2 7c0-3 5-5 10-5s10 2 10 5v2h-5V7.5c-1.5-.7-3.2-1-5-1s-3.5.3-5 1V9H2z"/><path d="M6 10l2-2h8l2 2 3 9H3z"/><circle cx="12" cy="15" r="2.6" fill="#fff"/></svg>
        <span>555 214 7730</span>
      </li>
      <li>
        <svg viewBox="0 0 24 22" aria-hidden="true"><path d="M6 1h10l2 2v7H6z"/><rect x="8" y="4" width="8" height="1.3" fill="#fff"/><rect x="8" y="6.5" width="8" height="1.3" fill="#fff"/><path d="M1 11h22v10H1z"/><rect x="4" y="16" width="16" height="1.6" fill="#fff"/></svg>
        <span>555 214 7731</span>
      </li>
    </ul>

    <ul class="contact-list contact-list--web">
      <li>
        <svg viewBox="0 0 24 22" aria-hidden="true"><path d="M1 5h22v13H1z"/><path d="M1.5 5.5L12 13l10.5-7.5" fill="none" stroke="#fff" stroke-width="1.8"/></svg>
        <span>info@redmontcreekoms.com</span>
      </li>
      <li>
        <svg viewBox="0 0 24 22" aria-hidden="true"><circle cx="12" cy="11" r="10"/><path d="M7 5c2 1 3 3 1 5s1 4 3 3 2 3 0 6c-3-1-5-4-5-8 0-2 .3-4 1-6zM15 4c2 1 4 3 4 5-2 0-3-1-4-2s-1-2 0-3z" fill="#fff"/></svg>
        <span>www.redmontcreekoms.com</span>
      </li>
    </ul>
  </section>
</main>
</body>
</html>
```